Flyer-Design für Software für Gebäudedienstleister
Zielgruppe
Software für Gebäudedienstleister,
Softwarevertrieb, Durchführung von Schulungen,
Aufgabenstellung
Erstellt werden soll eine Din A4 Seite mit Wickelfalz (6Seiten)
Für den Neustart einer Software für Gebäudedienstleister möchten wir einen modernen
Flyer mit ansprechendem Text anfertigen lassen.
Die Software funktioniert Online oder Lokal.
Ein Tablet-Service wird angeboten.
Eine elektronische Planungstafel bietet die Software.
Terminplanung mittels "Drag & Drop" möglich
1-Klick Funktion in der Rückmeldung von Arbeitsscheinen und in der anschließenden Fakturierung.
Durchführung von Schulungen Akademie
Texte:
1.Fakturierung
Mit Vantoruk® Faktura liefern wir Ihnen ein leicht zu bedienendes Modul
Die Vantoruk®Fakturierungssoftware zeichnet sich durch einfache Handhabung aus:
Moderne Faktura Software
Leicht zu bedienen
Gut strukturierte Benutzeroberfläche
Praxisorientierte Funktionen
Sofort einsatzbereit
1-Klick Fakturierung
Mit Vantoruk® fakturieren Sie schnell und effektiv.
2. Personaleinsatzplanung Drag & Drop
Die Einsatzplanung erfolgt in Vantoruk® mit nur wenigen Schritten.
Dabei berücksichtigt das System z.B. die Regionen, in denen Sie
tätig sind und verhindert somit unnötige Fahrzeiten.
Pausen werden automatisch erfasst. Touren planen Sie bereits
bequem per Drag & Drop auf dem Gesamtkalender.
3. Planungstafel
Mit Vantoruk® planen Sie einfach und schnell Termine.
Mit unserer elektronischen Planungstafel behalten Sie immer
einen optimalen Überblick über Ihre Ressourcen.
Vantoruk® ist die intelligente Lösung für Ihre Personaleinsatzplanung.
4. Tabletservice
Bieten Sie Ihrem Kunden mit Vantoruk® einen echten Mehrwert
Sie möchten Ihrem Kunden gegenüber als modernes und zielorientiertes
Unternehmen auftreten?
Setzen Sie ab jetzt unseren Tablet-Service in Ihrem Betrieb ein.
Egal ob Arbeitsschein zurückmelden, schnell ein Foto vom Wintergarten,
oder eine Unterschrift fü..

```html
<!DOCTYPE html>
<html lang="de">
<head>
<meta charset="utf-8">
<title>Vantoruk – Wickelfalz-Flyer</title>
<link href="https://fonts.googleapis.com/css2?family=Questrial&family=Montserrat:wght@500&display=swap" rel="stylesheet">
<style>
  :root{
    --green:#a9b935;
    --slate:#5b6076;
    --text:#6a6d7e;
    --paper:#ffffff;
    --bg:#ffffff;
    --label:#1f1f1f;
  }
  html,body{margin:0;padding:0;width:1200px;height:1200px;overflow:hidden;background:var(--bg);}
  .board{position:relative;width:1200px;height:1200px;font-family:"Questrial",sans-serif;}
  .sheet{position:absolute;background:var(--paper);filter:drop-shadow(0 3px 4px rgba(0,0,0,.28));}
  .view-label{position:absolute;font-family:"Montserrat",sans-serif;font-weight:500;font-size:26px;letter-spacing:2px;color:var(--label);}
  .defs{position:absolute;width:0;height:0;overflow:hidden;}
  svg text{font-family:"Questrial",sans-serif;}
  .t-head{font-size:32px;}
  .t-body{font-size:9.6px;fill:var(--text);}
  .t-small{font-size:6px;fill:var(--text);}
</style>
</head>
<body>
<div class="board">

<svg class="defs" aria-hidden="true">
  <defs>
    <linearGradient id="sky" x1="0" y1="0" x2="1" y2="1">
      <stop offset="0" stop-color="#8e9bb0"/><stop offset=".6" stop-color="#c9ced6"/><stop offset="1" stop-color="#a7acb2"/>
    </linearGradient>
    <linearGradient id="desk" x1="0" y1="0" x2="1" y2="1">
      <stop offset="0" stop-color="#e9eaec"/><stop offset="1" stop-color="#f6f6f7"/>
    </linearGradient>
    <linearGradient id="notes" x1="0" y1="0" x2="1" y2="1">
      <stop offset="0" stop-color="#b3c94a"/><stop offset=".5" stop-color="#8f9a6e"/><stop offset="1" stop-color="#c4d257"/>
    </linearGradient>
    <linearGradient id="office" x1="0" y1="0" x2="0" y2="1">
      <stop offset="0" stop-color="#c2c7cf"/><stop offset=".55" stop-color="#6a5a4e"/><stop offset="1" stop-color="#4f6b3a"/>
    </linearGradient>

    <g id="planner">
      <text x="0" y="0" style="font-size:5px;font-weight:bold" fill="#5b6076">Terminplaner</text>
      <g fill="var(--green)">
        <rect x="0" y="6" width="40" height="5"/><rect x="44" y="6" width="30" height="5"/>
        <rect x="78" y="6" width="16" height="5"/><rect x="98" y="6" width="8" height="5"/>
        <rect x="109" y="6" width="8" height="5"/><rect x="120" y="6" width="8" height="5"/>
        <rect x="131" y="6" width="8" height="5"/><rect x="225" y="6" width="8" height="5"/>
        <rect x="236" y="6" width="8" height="5"/><rect x="247" y="6" width="8" height="5"/>
        <rect x="258" y="6" width="8" height="5"/>
      </g>
      <rect x="0" y="18" width="290" height="76" fill="none" stroke="#c9ccd3" stroke-width=".6"/>
      <g fill="#f2d7db"><rect x="94" y="24" width="8" height="70"/><rect x="186" y="24" width="8" height="70"/></g>
      <g stroke="#d9dbe0" stroke-width=".4">
        <line x1="0" y1="24" x2="290" y2="24"/><line x1="0" y1="34" x2="290" y2="34"/>
        <line x1="0" y1="44" x2="290" y2="44"/><line x1="0" y1="54" x2="290" y2="54"/>
        <line x1="0" y1="64" x2="290" y2="64"/><line x1="0" y1="74" x2="290" y2="74"/>
        <line x1="0" y1="84" x2="290" y2="84"/>
        <line x1="58" y1="18" x2="58" y2="94"/><line x1="70" y1="18" x2="70" y2="94"/>
        <line x1="82" y1="18" x2="82" y2="94"/><line x1="106" y1="18" x2="106" y2="94"/>
        <line x1="118" y1="18" x2="118" y2="94"/><line x1="130" y1="18" x2="130" y2="94"/>
        <line x1="142" y1="18" x2="142" y2="94"/><line x1="154" y1="18" x2="154" y2="94"/>
        <line x1="166" y1="18" x2="166" y2="94"/><line x1="178" y1="18" x2="178" y2="94"/>
        <line x1="202" y1="18" x2="202" y2="94"/><line x1="214" y1="18" x2="214" y2="94"/>
        <line x1="226" y1="18" x2="226" y2="94"/><line x1="238" y1="18" x2="238" y2="94"/>
        <line x1="250" y1="18" x2="250" y2="94"/><line x1="262" y1="18" x2="262" y2="94"/>
        <line x1="274" y1="18" x2="274" y2="94"/>
      </g>
      <rect x="70" y="45" width="20" height="7" fill="#c9c79a"/>
      <rect x="100" y="55" width="24" height="7" fill="#aac8e2"/>
      <rect x="70" y="65" width="150" height="7" fill="#8fb8dd"/>
      <rect x="180" y="55" width="22" height="7" fill="#aac8e2"/>
      <rect x="228" y="45" width="20" height="7" fill="#c9c79a"/>
      <rect x="262" y="35" width="28" height="7" fill="#8fb8dd"/>
      <rect x="240" y="75" width="22" height="7" fill="#aac8e2"/>
    </g>

    <!-- Außenseite: Fakturierung | Rückseite | Titel -->
    <g id="outer">
      <rect width="948" height="671" fill="#fff"/>
      <polygon class="corner" points="246,0 316,0 316,95" fill="var(--slate)"/>
      <path d="M12 0 V64 H286" fill="none" stroke="var(--green)" stroke-width="1.2"/>
      <line x1="12" y1="0" x2="12" y2="64" stroke="var(--slate)" stroke-width="1"/>
      <text x="38" y="52" class="t-head" fill="var(--slate)">Fakturierung</text>
      <text class="t-body">
        <tspan x="25" y="113">Lorem ipsum dolor sit amet, consectetuer adipiscing</tspan>
        <tspan x="25" y="124.5">elit. Aenean commodo ligula eget dolor. Aenean</tspan>
        <tspan x="25" y="136">massa. Cum sociis natoque penatibus et magnis dis</tspan>
        <tspan x="25" y="147.5">parturient montes, nascetur ridiculus mus. Donec quam</tspan>
        <tspan x="25" y="159">felis, ultricies nec, pellentesque eu, pretium quis, sem.</tspan>
        <tspan x="25" y="170.5">Nulla consequat massa quis enim. Donec pede justo,</tspan>
        <tspan x="25" y="182">fringilla vel, aliquet nec, vulputate eget, arcu.</tspan>
      </text>
      <g class="t-body">
        <circle cx="28" cy="207" r="1.5" fill="var(--green)"/><text x="34" y="210" class="t-body">Lorem ipsum</text>
        <circle cx="28" cy="218.5" r="1.5" fill="var(--green)"/><text x="34" y="221.5" class="t-body">Lorem ipsum</text>
        <circle cx="28" cy="230" r="1.5" fill="var(--green)"/><text x="34" y="233" class="t-body">Lorem ipsum</text>
        <circle cx="28" cy="241.5" r="1.5" fill="var(--green)"/><text x="34" y="244.5" class="t-body">Lorem ipsum</text>
        <circle cx="28" cy="253" r="1.5" fill="var(--green)"/><text x="34" y="256" class="t-body">Lorem ipsum</text>
        <circle cx="28" cy="264.5" r="1.5" fill="var(--green)"/><text x="34" y="267.5" class="t-body">Lorem ipsum</text>
      </g>
      <text class="t-body">
        <tspan x="25" y="310">Lorem ipsum dolor sit amet, consectetuer adipiscing</tspan>
        <tspan x="25" y="321.5">elit. Aenean commodo ligula eget dolor. Aenean</tspan>
        <tspan x="25" y="333">massa. Cum sociis natoque penatibus et magnis dis</tspan>
        <tspan x="25" y="344.5">parturient montes, nascetur ridiculus mus. Donec quam</tspan>
        <tspan x="25" y="356">felis, ultricies nec, pellentesque eu, pretium quis, sem.</tspan>
      </text>
      <g role="img" aria-label="Foto: Arbeitsplatz mit Laptop, Monitor mit Balkendiagramm und Kaffeetasse">
        <rect x="0" y="420" width="316" height="237" fill="url(#desk)"/>
      </g>

      <g role="img" aria-label="Foto: moderne Bürogebäude mit geschwungener Glasfassade">
        <rect x="646" y="0" width="302" height="200" fill="url(#sky)"/>
      </g>
      <polygon points="316,312 606,600 534,671 316,671" fill="var(--slate)"/>
      <polygon points="948,312 948,671 727,671 648,592" fill="var(--slate)"/>
      <polygon points="633,30 899,296 633,562 366,296" fill="var(--green)"/>
      <polygon points="617,30 900,277 640,566 366,316" fill="none" stroke="var(--slate)" stroke-width="1"/>
      <g fill="#fff">
        <text x="641" y="216" style="font-size:50px">DIE</text>
        <text x="644" y="262" style="font-size:36px;letter-spacing:1px">Software</text>
        <text x="645" y="303" style="font-size:27px">für</text>
        <text x="645" y="340" style="font-size:30px;letter-spacing:.5px">Gebäude-</text>
        <text x="645" y="373" style="font-size:30px;letter-spacing:.5px">dienstleister</text>
        <circle cx="714" cy="582" r="9" fill="#fff"/>
        <text x="730" y="594" style="font-size:34px">Vantoruk</text>
        <text x="732" y="610" style="font-size:7px;letter-spacing:1.2px">SOFTWARE FÜR GEBÄUDEDIENSTLEISTER</text>
      </g>
    </g>

    <!-- Innenseite: Planungstafel / Drag & Drop | Mitarbeiterplanung | Academie / Tablettservice -->
    <g id="inner">
      <rect width="948" height="671" fill="#fff"/>
      <polygon points="0,0 16,0 48,32 0,64" fill="var(--green)"/>
      <path d="M30 64 H303 V0" fill="none" stroke="var(--slate)" stroke-width="1"/>
      <text x="82" y="42" class="t-head" fill="var(--green)">Planungstafel</text>
      <text class="t-body">
        <tspan x="22" y="106">Lorem ipsum dolor sit amet, consectetuer adipiscing elit.</tspan>
        <tspan x="22" y="117.5">Aenean commodo ligula eget dolor. Aenean massa. Cum</tspan>
        <tspan x="22" y="129">sociis natoque penatibus et magnis dis parturient montes,</tspan>
        <tspan x="22" y="140.5">nascetur ridiculus mus. Donec quam felis, ultricies nec,</tspan>
        <tspan x="22" y="152">pellentesque eu, pretium quis, sem. Nulla consequat mas-</tspan>
        <tspan x="22" y="163.5">sa quis enim. Donec pede justo, fringilla vel, aliquet nec,</tspan>
        <tspan x="22" y="175">vulputate eget, arcu.</tspan>
      </text>
      <use href="#planner" x="14" y="214"/>

      <polygon points="243,379 316,305 316,452" fill="var(--slate)"/>
      <path d="M243 379 H12 V443 H305" fill="none" stroke="var(--slate)" stroke-width="1"/>
      <line x1="12" y1="443" x2="305" y2="443" stroke="var(--green)" stroke-width="1.2"/>
      <text x="20" y="423" class="t-head" fill="var(--slate)">Drag &amp; Drop</text>
      <text class="t-body">
        <tspan x="25" y="489">Lorem ipsum dolor sit amet, consectetuer adipiscing</tspan>
        <tspan x="25" y="500.5">elit. Aenean commodo ligula eget dolor. Aenean</tspan>
        <tspan x="25" y="512">massa. Cum sociis natoque penatibus et magnis dis</tspan>
        <tspan x="25" y="523.5">parturient montes, nascetur ridiculus mus. Donec quam</tspan>
        <tspan x="25" y="535">felis, ultricies nec, pellentesque eu, pretium quis, sem.</tspan>
        <tspan x="25" y="546.5">Nulla consequat massa quis enim. Donec pede justo,</tspan>
        <tspan x="25" y="558">fringilla vel, aliquet nec, vulputate eget, arcu.</tspan>
      </text>
      <use href="#planner" x="14" y="584"/>

      <g role="img" aria-label="Foto: Mann hinter einer Glaswand mit grünen Haftnotizen">
        <rect x="330" y="0" width="302" height="185" fill="url(#notes)"/>
      </g>
      <polygon points="316,181 378,242 316,304" fill="var(--green)"/>
      <path d="M352 218 H632 V303 H316" fill="none" stroke="var(--slate)" stroke-width="1"/>
      <text x="425" y="255" class="t-head" fill="var(--green)">Mitarbeiter-</text>
      <text x="425" y="293" class="t-head" fill="var(--green)">planung</text>
      <text class="t-body">
        <tspan x="352" y="365">Lorem ipsum dolor sit amet, consectetuer adipiscing</tspan>
        <tspan x="352" y="376.5">elit. Aenean commodo ligula eget dolor. Aenean</tspan>
        <tspan x="352" y="388">massa. Cum sociis natoque penatibus et magnis dis</tspan>
        <tspan x="352" y="399.5">parturient montes, nascetur ridiculus mus. Donec</tspan>
        <tspan x="352" y="411">quam felis, ultricies nec, pellentesque eu, pretium</tspan>
        <tspan x="352" y="422.5">quis, sem. Nulla consequat massa quis enim. Donec</tspan>
        <tspan x="352" y="434">pede justo, fringilla vel, aliquet nec, vulputate eget,</tspan>
        <tspan x="352" y="445.5">arcu.</tspan>
        <tspan x="352" y="468">Lorem ipsum dolor sit amet, consectetuer adipiscing</tspan>
        <tspan x="352" y="479.5">elit. Aenean commodo ligula eget dolor. Aenean</tspan>
        <tspan x="352" y="491">massa. Cum sociis natoque penatibus et magnis dis</tspan>
        <tspan x="352" y="502.5">parturient montes, nascetur ridiculus mus. Donec</tspan>
        <tspan x="352" y="514">quam felis, ultricies nec, pellentesque eu, pretium</tspan>
        <tspan x="352" y="525.5">quis, sem. Nulla consequat massa quis enim. Donec</tspan>
        <tspan x="352" y="537">pede justo, fringilla vel, aliquet nec, vulputate eget,</tspan>
        <tspan x="352" y="548.5">arcu.</tspan>
      </text>

      <path d="M644 0 V64 H908" fill="none" stroke="var(--slate)" stroke-width="1"/>
      <line x1="644" y1="64" x2="908" y2="64" stroke="var(--green)" stroke-width="1.2"/>
      <polygon points="864,0 948,0 948,106" fill="var(--slate)"/>
      <text x="652" y="42" class="t-head" fill="var(--slate)">Academie</text>
      <text class="t-body">
        <tspan x="644" y="106">Lorem ipsum dolor sit amet, consectetuer adipiscing elit.</tspan>
        <tspan x="644" y="117.5">Aenean commodo ligula eget dolor. Aenean massa. Cum</tspan>
        <tspan x="644" y="129">sociis natoque penatibus et magnis dis parturient montes,</tspan>
        <tspan x="644" y="140.5">nascetur ridiculus mus. Donec quam felis, ultricies nec,</tspan>
      </text>
      <g fill="var(--slate)">
        <polygon points="685,173 689,177 685,181 681,177"/><text x="693" y="180" class="t-body">Schulung 1</text>
        <polygon points="685,191 689,195 685,199 681,195"/><text x="693" y="198" class="t-body">Schulung 2</text>
        <polygon points="685,209 689,213 685,217 681,213"/><text x="693" y="216" class="t-body">Schulung 3</text>
        <polygon points="685,227 689,231 685,235 681,231"/><text x="693" y="234" class="t-body">Schulung 4</text>
      </g>
      <g role="img" aria-label="Foto: modernes Bürogebäude mit Glasfassade und Rasenfläche">
        <rect x="644" y="275" width="291" height="114" fill="url(#office)"/>
      </g>
      <polygon points="631,411 693,473 631,535" fill="var(--green)"/>
      <path d="M668 448 H936 V525 H632" fill="none" stroke="var(--slate)" stroke-width="1"/>
      <text x="704" y="497" class="t-head" fill="var(--green)">Tablettservice</text>
      <text class="t-body">
        <tspan x="644" y="567">Lorem ipsum dolor sit amet,</tspan>
        <tspan x="644" y="578.5">consectetuer adipiscing elit.</tspan>
        <tspan x="644" y="590">Aenean commodo ligula eget</tspan>
        <tspan x="644" y="601.5">dolor. Aenean massa. Cum</tspan>
        <tspan x="644" y="613">sociis natoque penatibus et</tspan>
        <tspan x="644" y="624.5">magnis dis parturient montes,</tspan>
        <tspan x="644" y="636">nascetur ridiculus mus.</tspan>
      </text>
      <rect x="812" y="560" width="124" height="79" fill="var(--green)"/>
      <polygon points="936,570 936,639 866,639" fill="#c4d45c"/>
      <rect x="859" y="570" width="28" height="38" rx="3" fill="#fff" stroke="#333" stroke-width="2"/>
      <rect x="864" y="576" width="18" height="26" fill="#e5e8d8"/>
      <line x1="873" y1="612" x2="873" y2="630" stroke="#333" stroke-width="3"/>
    </g>
  </defs>
</svg>

<svg class="sheet" style="left:40px;top:35px" width="593" height="420" viewBox="0 0 948 671"><use href="#outer"/></svg>
<svg class="sheet" style="left:720px;top:35px" width="198" height="420" viewBox="632 0 316 671"><use href="#outer"/></svg>
<svg class="sheet" style="left:975px;top:35px" width="198" height="420" viewBox="316 0 316 671"><use href="#outer"/></svg>

<div class="view-label" style="left:67px;top:466px">aussen</div>
<div class="view-label" style="left:738px;top:472px">Titel</div>
<div class="view-label" style="left:996px;top:469px">Rückseite</div>

<svg class="sheet" style="left:40px;top:535px" width="593" height="420" viewBox="0 0 948 671"><use href="#inner"/></svg>
<div class="view-label" style="left:67px;top:976px">innen</div>

<svg class="sheet" style="left:720px;top:540px" width="198" height="420" viewBox="0 0 316 671"><use href="#inner"/></svg>
<svg class="sheet" style="left:918px;top:540px" width="198" height="420" viewBox="0 0 316 671"><use href="#outer"/></svg>
<div class="view-label" style="left:743px;top:1028px">1x aufgeklappt</div>

</div>
</body>
</html>
```